Award Winning Patient Support Program needs infographics designed

I need two infographics created for my website and my pitch decks. I have two services I offer. Each service has 6 elements to it. I developed and launched an innovative, coaching-based program to help patients better manage side effects and stress as a solution to a challenge that costs healthcare $600 billion annually and costs patients quality of life and reduces positive outcomes. One of the services, my Patient Adherence Training Program, trains healthcare professionals such as pharmacists, nurses, and doctors, to use coaching skills and a behavior change strategy I designed to help them better listen to, understand, and support patients. The program includes live training intensives, coaching skills development webinars, a customized coaching guide, video training and support documents library, side effect management plan, and confidential patient call review. The second program is my Patient Support Program - it provides patients texting/email support programs, peer mentor support, online group coaching program, side effect management plan, caregiver support, and stress reduction strategies. The program was one of 9 finalists for the 2018 Velmora T9 Pioneering Patient Support Prize and I was invited to resubmit again this year. The goal of the infographics is to visually illustrate the 6 core elements of the two programs. Adherence and behavior change require comprehensive solutions - therefore the programs have to be robust - but I need to simplify the introduction to what each program includes. Patients deserve better support and are often judged as being lazy when they stop taking medication or don't follow "doctor's orders" - when, in fact, it is a complex list of factors that cause non-adherence. My programs also give them skills to help them enjoy better quality of life. The infographic design I envisioned and mocked up uses icons and can include text naming each icon for clarity. I don't expect the infographic to rely on the image of each icon alone. Also, there is one program element that is the same for both - the side effect management plan - so, while there are 12 elements between the two programs, there will be 11 icons. I would need each of the 11 icons in separate files as well as in a file with the finished infographic so I can use the icons independent of the infographic when I go into detailed slides/breakdown of the elements. I have attached a mock up with notes and breaking out the icons. I have also attached the wireframe for the new landing page to show how the infographics will be featured on the web page. My Bright Lantern Path logo was designed using Pixgrove and I still love it and get compliments all the time so I'm turning to this process again and hoping for as great an experience and outcome!

Target Market(s)

Healthcare organizations and pharmaceutical companies

Industry/Entity Type

Pharmaceutical

Font styles to use
Sans Serif

Colors
0792cd
f37122
ffffff

Requirements
Must have
• Consistent design for each icon in the infographic, readable text description of each icon, originally created icons - please do not use the samples in the brief as they are just to give an idea - I do not own the copyright to them.
Should not have
• Don't be insensitive to gender/culture/diversity in choice of icons - needs to be non-specific or a diverse representation

```html
<!DOCTYPE html>
<html lang="en">
<head>
<meta charset="utf-8">
<title>Bright Lantern Path – Program Elements</title>
<link rel="stylesheet" href="https://fonts.googleapis.com/css2?family=Asap:wght@400;500;600&family=Oswald:wght@500&display=swap">
<style>
  :root {
    --brand-blue: #0792cd;
    --band-blue: #0a90cf;
    --brand-orange: #f37122;
    --seg-orange-light: #f7931e;
    --seg-orange: #f15a24;
    --seg-red: #e8262a;
    --seg-red-deep: #c41f33;
    --ring-red: #e0312b;
    --white: #ffffff;
    --people-light: #eef1f4;
    --people-mid: #d9dfe6;
  }
  * { box-sizing: border-box; margin: 0; padding: 0; }
  html, body { width: 1200px; height: 1016px; overflow: hidden; background: var(--white); }
  .infographic { position: relative; width: 1200px; height: 1016px; font-family: "Asap", sans-serif; }
  .wheels { position: absolute; left: 0; top: 0; width: 1200px; height: 666px; display: block; }
  .seg-label { font-family: "Asap", sans-serif; font-weight: 600; font-size: 17.5px; fill: var(--white); text-anchor: middle; }
  .brand-name { font-family: "Asap", sans-serif; font-weight: 500; font-size: 21px; fill: var(--seg-orange); text-anchor: middle; }
  .program-title {
    position: absolute; top: 596px; width: 600px; text-align: center;
    font-family: "Oswald", sans-serif; font-weight: 500; font-size: 29px;
    color: var(--brand-blue); letter-spacing: 0.2px; transform: scaleY(1.06);
  }
  .program-title--org { left: 7px; }
  .program-title--patient { left: 606px; }
  .icon-band { position: absolute; left: 0; top: 666px; width: 1200px; height: 350px; display: block; }
  .band-label { font-family: "Asap", sans-serif; font-weight: 500; font-size: 12.5px; fill: var(--white); text-anchor: middle; }
  .icon-white { color: var(--white); }
</style>
</head>
<body>
<main class="infographic">

  <svg width="0" height="0" style="position:absolute" aria-hidden="true">
    <defs>
      <linearGradient id="grad-warm" x1="0" y1="0" x2="1" y2="0">
        <stop offset="0" stop-color="#f47b20"/><stop offset="1" stop-color="#e8262a"/>
      </linearGradient>
      <linearGradient id="grad-orange" x1="0" y1="0" x2="1" y2="0">
        <stop offset="0" stop-color="#f7931e"/><stop offset="1" stop-color="#f04e23"/>
      </linearGradient>
      <linearGradient id="grad-red" x1="0" y1="0" x2="1" y2="0">
        <stop offset="0" stop-color="#e8262a"/><stop offset="1" stop-color="#c41f33"/>
      </linearGradient>
      <radialGradient id="grad-people" cx="0.5" cy="0.5" r="0.5">
        <stop offset="0" stop-color="#d9dfe6"/><stop offset="1" stop-color="#f4f6f8"/>
      </radialGradient>

      <symbol id="i-trainer" viewBox="0 0 48 48">
        <circle cx="12" cy="10" r="4.5" fill="currentColor"/>
        <rect x="7.5" y="16" width="9" height="14" rx="2" fill="currentColor"/>
        <rect x="7.5" y="29" width="3.8" height="14" fill="currentColor"/>
        <rect x="12.7" y="29" width="3.8" height="14" fill="currentColor"/>
        <rect x="21" y="4" width="24" height="18" fill="none" stroke="currentColor" stroke-width="2.5"/>
        <line x1="15" y1="19" x2="31" y2="14" stroke="currentColor" stroke-width="2"/>
        <polyline points="26,17 31,12 35,14 40,8" fill="none" stroke="currentColor" stroke-width="1.6"/>
      </symbol>

      <symbol id="i-laptop" viewBox="0 0 48 48">
        <rect x="7" y="8" width="34" height="23" rx="2" fill="none" stroke="currentColor" stroke-width="2.5"/>
        <path d="M3 34h42l-3 5H6z" fill="currentColor"/>
        <circle cx="15" cy="15.5" r="2.6" fill="currentColor"/>
        <rect x="12.6" y="19" width="5" height="9" rx="1" fill="currentColor"/>
        <rect x="21" y="12" width="15" height="10" fill="none" stroke="currentColor" stroke-width="1.6"/>
        <line x1="17" y1="21" x2="25" y2="18" stroke="currentColor" stroke-width="1.4"/>
      </symbol>

      <symbol id="i-book" viewBox="0 0 48 48">
        <path fill-rule="evenodd" fill="currentColor" d="M13 4h26v38H13a5 5 0 0 1-5-5V9a5 5 0 0 1 5-5zM35 14L22 24l13 10z"/>
        <line x1="13" y1="8" x2="13" y2="38" stroke="currentColor" stroke-width="0"/>
      </symbol>

      <symbol id="i-video" viewBox="0 0 48 48">
        <rect x="4" y="8" width="40" height="32" rx="3" fill="none" stroke="currentColor" stroke-width="2.5"/>
        <line x1="4" y1="15" x2="44" y2="15" stroke="currentColor" stroke-width="2"/>
        <circle cx="9" cy="11.5" r="1.2" fill="currentColor"/>
        <circle cx="13" cy="11.5" r="1.2" fill="currentColor"/>
        <circle cx="17" cy="11.5" r="1.2" fill="currentColor"/>
        <circle cx="24" cy="27.5" r="7.5" fill="none" stroke="currentColor" stroke-width="2.5"/>
        <path d="M21.5 23.5v8l6.5-4z" fill="currentColor"/>
      </symbol>

      <symbol id="i-clipboard" viewBox="0 0 48 48">
        <rect x="10" y="8" width="28" height="37" rx="3" fill="none" stroke="currentColor" stroke-width="2.5"/>
        <rect x="17.5" y="4" width="13" height="7.5" rx="2" fill="currentColor"/>
        <rect x="15" y="17" width="3.5" height="3.5" fill="currentColor"/>
        <rect x="21" y="17.8" width="12" height="2" fill="currentColor"/>
        <rect x="15" y="23.5" width="3.5" height="3.5" fill="currentColor"/>
        <rect x="21" y="24.3" width="12" height="2" fill="currentColor"/>
        <rect x="15" y="30" width="3.5" height="3.5" fill="currentColor"/>
        <rect x="21" y="30.8" width="12" height="2" fill="currentColor"/>
        <rect x="15" y="36.5" width="3.5" height="3.5" fill="currentColor"/>
        <rect x="21" y="37.3" width="12" height="2" fill="currentColor"/>
      </symbol>

      <symbol id="i-confidential" viewBox="0 0 48 48">
        <path d="M3 20a10 10 0 0 1 10-10h6" fill="none" stroke="currentColor" stroke-width="2.5"/>
        <path d="M45 28a10 10 0 0 1-10 10h-6" fill="none" stroke="currentColor" stroke-width="2.5"/>
        <path d="M4 24h7v16H4z" fill="currentColor"/>
        <path d="M37 8h7v16h-7z" fill="currentColor"/>
        <path d="M19 21v-4a5 5 0 0 1 10 0v4" fill="none" stroke="currentColor" stroke-width="2.5"/>
        <rect x="16" y="21" width="16" height="13" rx="2" fill="currentColor"/>
      </symbol>

      <symbol id="i-texting" viewBox="0 0 48 48">
        <rect x="7" y="3" width="22" height="40" rx="3" fill="none" stroke="currentColor" stroke-width="2.5"/>
        <line x1="15" y1="38" x2="21" y2="38" stroke="currentColor" stroke-width="2"/>
        <path d="M14 9h20a3 3 0 0 1 3 3v9a3 3 0 0 1-3 3H22l-5 4v-4h-3a3 3 0 0 1-3-3v-9a3 3 0 0 1 3-3z" fill="currentColor"/>
        <rect x="29" y="28" width="17" height="12" fill="none" stroke="currentColor" stroke-width="2"/>
        <polyline points="29,28 37.5,35 46,28" fill="none" stroke="currentColor" stroke-width="2"/>
      </symbol>

      <symbol id="i-peers" viewBox="0 0 48 48">
        <circle cx="15" cy="12" r="6" fill="currentColor"/>
        <path d="M4 40v-8a11 11 0 0 1 22 0v8z" fill="currentColor"/>
        <circle cx="33" cy="13" r="5.5" fill="currentColor"/>
        <path d="M24 40v-7a10 10 0 0 1 20 0v7z" fill="currentColor"/>
      </symbol>

      <symbol id="i-caregiver" viewBox="0 0 48 48">
        <circle cx="24" cy="9" r="6" fill="currentColor"/>
        <path d="M24 41C11 32 9 22 16 19.5c4-1.4 7 1 8 3.5 1-2.5 4-4.9 8-3.5 7 2.5 5 12.5-8 21.5z" fill="currentColor"/>
        <path d="M6 24q3 12 18 19q15-7 18-19" fill="none" stroke="currentColor" stroke-width="3"/>
      </symbol>

      <symbol id="i-stress" viewBox="0 0 48 48">
        <circle cx="24" cy="9" r="6" fill="currentColor"/>
        <path d="M16 32q0-14 8-14t8 14z" fill="currentColor"/>
        <ellipse cx="24" cy="35" rx="17" ry="5.5" fill="currentColor"/>
      </symbol>

      <g id="wheel-ring">
        <path d="M-141.5,-245.1 A283 283 0 0 1 141.5,-245.1 L64,-110.9 A128 128 0 0 0 -64,-110.9Z" fill="url(#grad-warm)"/>
        <path d="M141.5,-245.1 A283 283 0 0 1 283,0 L128,0 A128 128 0 0 0 64,-110.9Z" fill="url(#grad-red)"/>
        <path d="M283,0 A283 283 0 0 1 141.5,245.1 L64,110.9 A128 128 0 0 0 128,0Z" fill="url(#grad-red)"/>
        <path d="M141.5,245.1 A283 283 0 0 1 -141.5,245.1 L-64,110.9 A128 128 0 0 0 64,110.9Z" fill="url(#grad-warm)"/>
        <path d="M-141.5,245.1 A283 283 0 0 1 -283,0 L-128,0 A128 128 0 0 0 -64,110.9Z" fill="url(#grad-orange)"/>
        <path d="M-283,0 A283 283 0 0 1 -141.5,-245.1 L-64,-110.9 A128 128 0 0 0 -128,0Z" fill="url(#grad-orange)"/>
        <g stroke="#ffffff" stroke-width="26">
          <line x1="-300" y1="0" x2="300" y2="0"/>
          <line x1="-150" y1="-259.8" x2="150" y2="259.8"/>
          <line x1="150" y1="-259.8" x2="-150" y2="259.8"/>
        </g>
      </g>

      <g id="badge">
        <circle r="40" fill="none" stroke="var(--ring-red)" stroke-width="3"/>
        <circle r="36" fill="var(--brand-orange)" stroke="#ffffff" stroke-width="4"/>
      </g>
    </defs>
  </svg>

  <svg class="wheels" viewBox="0 0 1240 688" aria-label="Program element wheels">
    <!-- brand -->
    <g class="brand">
      <circle cx="616" cy="46" r="22" fill="var(--brand-orange)"/>
      <text class="brand-name" x="616" y="98">Bright Lantern</text>
      <text class="brand-name" x="616" y="121">Path</text>
    </g>

    <!-- organizational wheel -->
    <g class="wheel wheel--org">
      <use href="#wheel-ring" transform="translate(317 313)"/>
      <g role="img" aria-label="Illustration of a diverse group of healthcare professionals: doctors, nurses and pharmacists">
        <ellipse cx="317" cy="313" rx="112" ry="70" fill="url(#grad-people)"/>
      </g>
      <g class="icon-white">
        <use href="#i-trainer" x="290" y="50" width="56" height="56"/>
        <use href="#i-laptop" x="460" y="143" width="60" height="60"/>
        <use href="#i-book" x="476" y="352" width="56" height="56"/>
        <use href="#i-video" x="287" y="462" width="62" height="62"/>
        <use href="#i-clipboard" x="94" y="347" width="58" height="62"/>
        <use href="#i-confidential" x="110" y="143" width="64" height="60"/>
      </g>
      <text class="seg-label" x="318" y="139">Live Training</text>
      <text class="seg-label" x="318" y="162">Intensives</text>
      <text class="seg-label" x="512" y="235">Coaching Skills</text>
      <text class="seg-label" x="512" y="258">Development</text>
      <text class="seg-label" x="512" y="282">Webinars</text>
      <text class="seg-label" x="489" y="446">Customized</text>
      <text class="seg-label" x="489" y="469">Coaching</text>
      <text class="seg-label" x="489" y="492">Guide</text>
      <text class="seg-label" x="320" y="550">Video Training</text>
      <text class="seg-label" x="320" y="573">Library</text>
      <text class="seg-label" x="143" y="447">Side Effect</text>
      <text class="seg-label" x="143" y="470">Management</text>
      <text class="seg-label" x="143" y="493">Plan</text>
      <text class="seg-label" x="116" y="233">Confidential</text>
      <text class="seg-label" x="116" y="256">Patient</text>
      <text class="seg-label" x="116" y="279">Call Review</text>
    </g>

    <!-- patient wheel -->
    <g class="wheel wheel--patient">
      <use href="#wheel-ring" transform="translate(923 313)"/>
      <g role="img" aria-label="Illustration of a diverse group of patients">
        <ellipse cx="923" cy="313" rx="112" ry="70" fill="url(#grad-people)"/>
      </g>
      <g class="icon-white">
        <use href="#i-texting" x="890" y="44" width="62" height="62"/>
        <use href="#i-peers" x="1066" y="148" width="62" height="62"/>
        <use href="#i-laptop" x="1084" y="350" width="62" height="62"/>
        <use href="#i-clipboard" x="895" y="456" width="58" height="62"/>
        <use href="#i-caregiver" x="698" y="350" width="66" height="66"/>
        <use href="#i-stress" x="712" y="136" width="62" height="62"/>
      </g>
      <text class="seg-label" x="918" y="135">Texting &amp;</text>
      <text class="seg-label" x="918" y="159">Email Support</text>
      <text class="seg-label" x="1120" y="241">Peer Mentor</text>
      <text class="seg-label" x="1120" y="265">Support</text>
      <text class="seg-label" x="1092" y="442">Online Group</text>
      <text class="seg-label" x="1092" y="465">Coaching</text>
      <text class="seg-label" x="1092" y="488">Program</text>
      <text class="seg-label" x="922" y="543">Side Effect</text>
      <text class="seg-label" x="922" y="566">Management Plan</text>
      <text class="seg-label" x="748" y="454">Caregiver</text>
      <text class="seg-label" x="748" y="478">Support</text>
      <text class="seg-label" x="724" y="232">Stress</text>
      <text class="seg-label" x="724" y="255">Reduction</text>
      <text class="seg-label" x="724" y="279">Strategies</text>
    </g>
  </svg>

  <h2 class="program-title program-title--org">ORGANIZATIONAL TRAINING &amp; RESOURCES</h2>
  <h2 class="program-title program-title--patient">PATIENT SUPPORT RESOURCES</h2>

  <svg class="icon-band" viewBox="0 688 1240 362" aria-label="Program element icons">
    <rect x="0" y="688" width="1240" height="362" fill="var(--band-blue)"/>
    <line x1="620" y1="730" x2="620" y2="1016" stroke="#ffffff" stroke-width="2"/>

    <g class="band-group band-group--org">
      <use href="#badge" transform="translate(182 775)"/>
      <use href="#badge" transform="translate(308 775)"/>
      <use href="#badge" transform="translate(430 775)"/>
      <use href="#badge" transform="translate(182 925)"/>
      <use href="#badge" transform="translate(308 925)"/>
      <use href="#badge" transform="translate(430 925)"/>
      <g class="icon-white">
        <use href="#i-trainer" x="160" y="753" width="44" height="44"/>
        <use href="#i-book" x="286" y="753" width="44" height="44"/>
        <use href="#i-clipboard" x="408" y="752" width="44" height="46"/>
        <use href="#i-laptop" x="159" y="902" width="46" height="46"/>
        <use href="#i-video" x="285" y="902" width="46" height="46"/>
        <use href="#i-confidential" x="406" y="902" width="48" height="46"/>
      </g>
      <text class="band-label" x="182" y="833">Live Training</text>
      <text class="band-label" x="182" y="850">Intensives</text>
      <text class="band-label" x="307" y="833">Customized</text>
      <text class="band-label" x="307" y="850">Coaching</text>
      <text class="band-label" x="307" y="867">Guide</text>
      <text class="band-label" x="430" y="833">Side Effect</text>
      <text class="band-label" x="430" y="850">Management</text>
      <text class="band-label" x="430" y="867">Plan</text>
      <text class="band-label" x="181" y="983">Coaching Skills</text>
      <text class="band-label" x="181" y="1000">Development</text>
      <text class="band-label" x="181" y="1017">Webinars</text>
      <text class="band-label" x="307" y="983">Video Training</text>
      <text class="band-label" x="307" y="1000">Library</text>
      <text class="band-label" x="430" y="983">Confidential</text>
      <text class="band-label" x="430" y="1000">Patient</text>
      <text class="band-label" x="430" y="1017">Call Review</text>
    </g>

    <g class="band-group band-group--patient">
      <use href="#badge" transform="translate(800 775)"/>
      <use href="#badge" transform="translate(919 775)"/>
      <use href="#badge" transform="translate(1038 775)"/>
      <use href="#badge" transform="translate(800 925)"/>
      <use href="#badge" transform="translate(919 925)"/>
      <use href="#badge" transform="translate(1038 925)"/>
      <g class="icon-white">
        <use href="#i-texting" x="777" y="752" width="46" height="46"/>
        <use href="#i-peers" x="896" y="752" width="46" height="46"/>
        <use href="#i-laptop" x="1015" y="752" width="46" height="46"/>
        <use href="#i-clipboard" x="778" y="902" width="44" height="46"/>
        <use href="#i-caregiver" x="896" y="902" width="46" height="46"/>
        <use href="#i-stress" x="1015" y="902" width="46" height="46"/>
      </g>
      <text class="band-label" x="800" y="833">Texting &amp;</text>
      <text class="band-label" x="800" y="850">Email Support</text>
      <text class="band-label" x="919" y="834">Peer Mentor</text>
      <text class="band-label" x="919" y="851">Support</text>
      <text class="band-label" x="1038" y="833">Online Group</text>
      <text class="band-label" x="1038" y="850">Coaching</text>
      <text class="band-label" x="1038" y="867">Program</text>
      <text class="band-label" x="800" y="982">Side Effect</text>
      <text class="band-label" x="800" y="999">Management</text>
      <text class="band-label" x="800" y="1016">Plan</text>
      <text class="band-label" x="919" y="982">Caregiver</text>
      <text class="band-label" x="919" y="999">Support</text>
      <text class="band-label" x="1038" y="982">Stress Reduction</text>
      <text class="band-label" x="1038" y="999">Strategies</text>
    </g>
  </svg>

</main>
</body>
</html>
```